Brightloom Reach - Business Card

We need a business card for a Social Media Marketing company that specializes in online marketing for small businesses in Canada using common Social Media platforms such as Instagram, Facebook, Snapchat & Twitter.

I have uploaded a copy of our logo which I would like utilized in the business card. We would like the business card to be modern yet classy design.

Our website is www.brightloomreach.ca

Industry/Entity Type

Marketing

Contact Information for Business Card

Email: info@brightloomreach.ca
Website: www.brightloomreach.ca
Telephone: 604-352-9081

Colors

Designer to choose colors to be used in the design.

Requirements
Must have
• Social Media icons on reverse
• Please add some designs with color.

```html
<!DOCTYPE html>
<html lang="en">
<head>
<meta charset="utf-8">
<title>Brightloom Reach – Business Card</title>
<link href="https://fonts.googleapis.com/css2?family=Lato:wght@400;700;900&display=swap" rel="stylesheet">
<style>
  :root {
    --bg: #2b2b2b;
    --card-dark: #262626;
    --card-light: #ffffff;
    --ink-dark: #2e2e2e;
    --ink-mid: #3a3a3a;
    --ink-light: #f2f2f2;
    --logo-on-dark: #6a6a6a;
    --decor: #ececee;
    --accent-1: #c13584;
    --accent-2: #3b5998;
    --accent-3: #f5e100;
    --accent-4: #3a9ad9;
  }
  * { margin: 0; padding: 0; box-sizing: border-box; }
  html, body { width: 1200px; height: 880px; overflow: hidden; }
  body {
    background: var(--bg);
    font-family: 'Lato', sans-serif;
    position: relative;
  }
  .card {
    position: absolute;
    width: 560px;
    height: 320px;
    border-radius: 18px;
    overflow: hidden;
  }
  .card--front {
    left: 90px; top: 80px;
    background: var(--card-dark);
  }
  .card--back {
    left: 550px; top: 460px;
    background: var(--card-light);
  }
  .wordmark {
    font-family: 'Lato', sans-serif;
    font-weight: 900;
    text-transform: uppercase;
    letter-spacing: 1px;
    line-height: 1.05;
    text-align: center;
  }
  .card--front .wordmark {
    position: absolute;
    left: 0; right: 0; top: 92px;
    font-size: 38px;
    color: var(--logo-on-dark);
  }
  .tagline {
    font-size: 15px;
    letter-spacing: 0.3px;
  }
  .card--front .tagline {
    position: absolute;
    left: 0; right: 0; top: 236px;
    text-align: center;
    color: var(--ink-light);
  }
  .decor-area {
    position: absolute;
    left: 30px; top: 40px;
    width: 290px; height: 200px;
    background: var(--decor);
    border-radius: 40px;
    opacity: 0.7;
  }
  .card--back .wordmark {
    position: absolute;
    right: 34px; top: 34px;
    width: 230px;
    font-size: 32px;
    color: var(--ink-dark);
  }
  .social-row {
    position: absolute;
    right: 34px; top: 132px;
    display: flex; gap: 10px;
  }
  .social-row span {
    width: 28px; height: 28px;
    border-radius: 7px;
    display: block;
  }
  .social-row .s1 { background: var(--accent-1); }
  .social-row .s2 { background: var(--accent-2); }
  .social-row .s3 { background: var(--accent-3); }
  .social-row .s4 { background: var(--accent-4); }
  .contact {
    position: absolute;
    left: 34px; bottom: 32px;
    color: var(--ink-mid);
  }
  .contact .person-name {
    font-weight: 700;
    font-size: 22px;
    letter-spacing: 0.5px;
    color: var(--ink-dark);
    margin-bottom: 10px;
  }
  .contact .line {
    font-size: 14px;
    line-height: 1.5;
  }
  .contact .line b { font-weight: 700; }
  .contact .tagline { margin-top: 8px; font-size: 14px; }
</style>
</head>
<body>
  <section class="card card--front">
    <div class="wordmark">Brightloom<br>Reach</div>
    <p class="tagline">Connecting Your Business To Your Community</p>
  </section>

  <section class="card card--back">
    <div class="decor-area" role="img" aria-label="Faint textured brand decoration"></div>
    <div class="wordmark">Brightloom<br>Reach</div>
    <div class="social-row" aria-label="Social media profiles">
      <span class="s1"></span><span class="s2"></span><span class="s3"></span><span class="s4"></span>
    </div>
    <div class="contact">
      <p class="person-name">JORDAN HALE</p>
      <p class="line"><b>P:</b> 604-352-9081 | <b>E:</b> info@brightloomreach.ca</p>
      <p class="line"><b>W:</b> www.brightloomreach.ca</p>
      <p class="tagline">Connecting Your Business To Your Community</p>
    </div>
  </section>
</body>
</html>
```